Business card Zottelgarten

Business card is for a self-employed dog trainer with own dog school. Name and logo of the dog school are available. Color specifications as well. The design should be classy and minimalist, but also modern. An already existing idea would be: Front: Only the logo Back: Contact data

Font styles to use
Serif
Sans Serif
Other font styles liked:
• Trajan Pro

Colors
f78f20

Requirements
Must have
• Name: Margit Wendler-Rasch Title: Dipl. Dog Trainer Contain my logo Follow my font and color preferences (see files)

```html
<!DOCTYPE html>
<html lang="de">
<head>
<meta charset="utf-8">
<title>Zottelgarten – Visitenkarte</title>
<link rel="stylesheet" href="https://fonts.googleapis.com/css2?family=Cinzel:wght@400&family=Open+Sans:wght@400;600&display=swap">
<style>
  :root {
    --backdrop: #2a2a2a;
    --paper: #fbfbfb;
    --brown: #76604f;
    --brown-card: #7a6555;
    --cream: #f4efe9;
    --orange: #f78f20;
    --ink: #5b4f46;
    --grey: #6e6e6e;
  }
  * { margin: 0; padding: 0; box-sizing: border-box; }
  html, body {
    width: 1200px; height: 800px; overflow: hidden;
    background: var(--backdrop);
  }
  .canvas {
    position: relative; width: 1200px; height: 800px;
  }
  .card {
    position: absolute; left: 320px; width: 560px; height: 320px;
    box-shadow: 0 12px 30px rgba(0,0,0,.45);
  }

  /* Contact side */
  .card--contact { top: 40px; background: var(--paper); }
  .brand {
    position: absolute; left: 48px; top: 30px;
    display: flex; flex-direction: column; align-items: center; width: 220px;
  }
  .brand__circle {
    width: 104px; height: 104px; border-radius: 50%;
    border: 2px solid var(--brown);
  }
  .brand__name {
    margin-top: 10px;
    font-family: "Cinzel", serif; font-size: 25px; letter-spacing: 1.5px;
    color: var(--brown);
  }
  .rule {
    position: absolute; height: 1.5px; background: var(--brown);
  }
  .rule--long { left: 48px; top: 178px; width: 300px; }
  .rule--short { left: 528px; top: 152px; width: 32px; }
  .person {
    position: absolute; right: 40px; top: 138px; text-align: right;
    font-family: "Open Sans", sans-serif;
  }
  .person__name { font-size: 17px; font-weight: 600; color: var(--orange); line-height: 1.2; }
  .person__title { font-size: 10px; color: var(--grey); }
  .contacts {
    position: absolute; left: 48px; top: 210px; list-style: none;
    font-family: "Open Sans", sans-serif; font-size: 11.5px; color: var(--ink);
  }
  .contacts li { display: flex; align-items: center; gap: 9px; height: 21px; }
  .contacts svg { width: 11px; height: 11px; fill: var(--orange); flex: none; }

  /* Logo side */
  .card--logo {
    top: 440px; background: var(--brown-card);
    display: flex; flex-direction: column; align-items: center;
  }
  .emblem {
    margin-top: 34px; width: 150px; height: 150px; border-radius: 50%;
    background: var(--cream); box-shadow: 0 0 0 3px var(--brown-card), 0 0 0 4.5px var(--cream);
  }
  .wordmark {
    margin-top: 22px;
    font-family: "Cinzel", serif; font-size: 44px; letter-spacing: 3px;
    color: var(--cream); line-height: 1;
  }
  .web {
    margin-top: 8px;
    font-family: "Cinzel", serif; font-size: 11px; letter-spacing: 6px;
    color: var(--cream);
  }
</style>
</head>
<body>
<main class="canvas">

  <section class="card card--contact">
    <div class="brand">
      <div class="brand__circle"></div>
      <div class="brand__name">ZOTTELGARTEN</div>
    </div>
    <div class="rule rule--long"></div>
    <div class="person">
      <div class="person__name">Margit Wendler-Rasch</div>
      <div class="person__title">Dipl. Dog Trainer</div>
    </div>
    <div class="rule rule--short"></div>
    <ul class="contacts">
      <li>
        <svg viewBox="0 0 24 24" aria-hidden="true"><path d="M6.6 10.8a15 15 0 0 0 6.6 6.6l2.2-2.2c.3-.3.7-.4 1-.2 1.1.4 2.3.6 3.6.6.6 0 1 .4 1 1V20c0 .6-.4 1-1 1A17 17 0 0 1 3 4c0-.6.4-1 1-1h3.5c.6 0 1 .4 1 1 0 1.3.2 2.5.6 3.6.1.3 0 .7-.2 1z"/></svg>
        000 987 6543
      </li>
      <li>
        <svg viewBox="0 0 24 24" aria-hidden="true"><path d="M2 5h20v14H2z M2 5l10 7 10-7" /></svg>
        info@zottelgarten.ch
      </li>
      <li>
        <svg viewBox="0 0 24 24" aria-hidden="true"><circle cx="12" cy="12" r="10"/></svg>
        www.zottelgarten.ch
      </li>
      <li>
        <svg viewBox="0 0 24 24" aria-hidden="true"><rect x="3" y="3" width="18" height="18" rx="3"/></svg>
        @zottelgarten
      </li>
    </ul>
  </section>

  <section class="card card--logo">
    <div class="emblem"></div>
    <div class="wordmark">ZOTTELGARTEN</div>
    <div class="web">WWW.ZOTTELGARTEN.CH</div>
  </section>

</main>
</body>
</html>
```